Tolvane Air Center needs a new upscale business card design for our high end aircraft hangar complex

Tolvane Air Center (TAC) is a large, upscale jet hangar complex in the US housing expensive aircraft. We need a new business card design, using our current logo. We will be attending a industry convention and need a card design that will stand out and be remembered by aircraft owners and private pilots.

Target Market(s)

Aircraft pilots or owners looking for a new upscale hangar

Industry/Entity Type

Airport

I like to use very heavy card stock, 400#, double sided. Square, no rounded edges please.

Colors
3276b5
0255a3
85abd2

Requirements
Must have
• An expensive, classy design, vivid colors.
Nice to have
• Needs to look very expensive and classy, and have some "pop". Designer must be able to download or copy my current typeface or fonts.
• One card side might be black with the "Logo and Tolvane Air Center Double line image in blue (or try gold, or glossy black), and perhaps have a grayed out "R470 jet silhouette". The other card side would have our contact info, and perhaps the "TAC Logo only". I'd like my contact info 'stacked', not in a paragraph format.
Should not have
• Should not look "too busy". Having a double-sided card will help.

```html
<!DOCTYPE html>
<html lang="en">
<head>
<meta charset="utf-8">
<title>Tolvane Air Center – Business Card</title>
<link href="https://fonts.googleapis.com/css2?family=Arimo:wght@400;700&display=swap" rel="stylesheet">
<style>
  :root {
    --page-bg: #e8e8e8;
    --card-core: #2c2c2c;
    --card-edge: #0f0f0f;
    --brand-blue: #1f5aa0;
    --text-light: #c9c9c9;
    --text-soft: #bdbdbd;
    --rule-gray: #6a6a6a;
    --icon-gray: #c4c4c4;
    --jet-gray: #5a5a5a;
  }
  * { margin: 0; padding: 0; box-sizing: border-box; }
  html, body {
    width: 952px;
    height: 1200px;
    overflow: hidden;
    background: var(--page-bg);
    font-family: "Arimo", Arial, sans-serif;
  }
  .canvas { position: relative; width: 952px; height: 1200px; }
  .card {
    position: absolute;
    width: 739px;
    background: radial-gradient(ellipse at 50% 45%, var(--card-core) 0%, #1c1c1c 55%, var(--card-edge) 100%);
  }
  .card--front { left: 109px; top: 120px; height: 422px; }
  .card--back  { left: 111px; top: 643px; height: 429px; }

  /* Front */
  .brand {
    position: absolute;
    left: 0; right: 0; top: 0; bottom: 0;
    display: flex;
    align-items: center;
    justify-content: center;
    gap: 18px;
    color: var(--brand-blue);
    font-weight: 700;
  }
  .brand__mark {
    width: 26px; height: 26px;
    border-radius: 50%;
    background: var(--brand-blue);
    flex: none;
  }
  .brand__name {
    font-size: 46px;
    line-height: 1;
    letter-spacing: 2px;
    white-space: nowrap;
  }

  /* Back */
  .accent-rule {
    position: absolute;
    left: 0; top: 58px;
    width: 291px; height: 10px;
    background: var(--rule-gray);
  }
  .person {
    position: absolute;
    left: 369px; width: 320px; top: 52px;
    text-align: center;
    color: var(--text-light);
    font-weight: 700;
  }
  .person__name { font-size: 38px; line-height: 1; letter-spacing: 0.5px; white-space: nowrap; }
  .person__role { font-size: 29px; line-height: 1; margin-top: 8px; color: var(--text-soft); }

  .contacts { position: absolute; left: 43px; top: 150px; list-style: none; }
  .contacts__item {
    position: absolute;
    display: flex; align-items: center;
    height: 28px;
    font-size: 17px;
    color: var(--text-soft);
  }
  .contacts__icon { width: 30px; height: 28px; margin-right: 18px; flex: none; }
  .contacts__item--email { top: 0; }
  .contacts__item--phone { top: 62px; }
  .contacts__item--place { top: 119px; }
  .contacts__item--web   { top: 185px; }
  .contacts__item span { white-space: nowrap; }

  .jet-silhouette {
    position: absolute;
    left: 368px; top: 262px;
    width: 324px; height: 98px;
    background: radial-gradient(ellipse at 50% 70%, var(--jet-gray) 0%, rgba(70,70,70,0.5) 35%, rgba(40,40,40,0) 75%);
  }
</style>
</head>
<body>
<main class="canvas">

  <section class="card card--front" aria-label="Card front">
    <div class="brand">
      <span class="brand__mark"></span>
      <span class="brand__name">TOLVANE AIR CENTER</span>
    </div>
  </section>

  <section class="card card--back" aria-label="Card back">
    <div class="accent-rule"></div>

    <div class="person">
      <div class="person__name">DANE KERROW</div>
      <div class="person__role">Director</div>
    </div>

    <ul class="contacts">
      <li class="contacts__item contacts__item--email">
        <svg class="contacts__icon" viewBox="0 0 30 28" aria-hidden="true">
          <rect x="1" y="6" width="28" height="17" fill="none" stroke="var(--icon-gray)" stroke-width="2"/>
          <path d="M1 6 L15 17 L29 6 M1 23 L11 14 M29 23 L19 14" fill="none" stroke="var(--icon-gray)" stroke-width="2"/>
        </svg>
        <span>hangar@tolvaneair.net</span>
      </li>
      <li class="contacts__item contacts__item--phone">
        <svg class="contacts__icon" viewBox="0 0 30 28" aria-hidden="true">
          <path d="M9 3 L13 8 L10.5 11 Q12 17 17.5 20.5 L20.5 18 L25 22 L22 26 Q10 24 6 8 Z" fill="var(--icon-gray)"/>
        </svg>
        <span>555 270 418</span>
      </li>
      <li class="contacts__item contacts__item--place">
        <svg class="contacts__icon" viewBox="0 0 30 28" aria-hidden="true">
          <path d="M15 1 C9 1 6 5.5 6 10 C6 16 15 27 15 27 C15 27 24 16 24 10 C24 5.5 21 1 15 1 Z" fill="var(--icon-gray)"/>
          <circle cx="15" cy="10" r="3.5" fill="#1c1c1c"/>
        </svg>
        <span>418, Birch Field, 24810 NY</span>
      </li>
      <li class="contacts__item contacts__item--web">
        <svg class="contacts__icon" viewBox="0 0 30 28" aria-hidden="true">
          <g fill="none" stroke="var(--icon-gray)" stroke-width="1.8">
            <circle cx="15" cy="14" r="12"/>
            <ellipse cx="15" cy="14" rx="5.5" ry="12"/>
            <line x1="3" y1="14" x2="27" y2="14"/>
            <line x1="5" y1="8" x2="25" y2="8"/>
            <line x1="5" y1="20" x2="25" y2="20"/>
          </g>
        </svg>
        <span>www.tolvaneair.net</span>
      </li>
    </ul>

    <div class="jet-silhouette" role="img" aria-label="Grayed front-view silhouette of a business jet"></div>
  </section>

</main>
</body>
</html>
```